Online-Marketing Material für Autohaus mit Werkstätten
Zielgruppe
Wir betreiben ein Autohaus mit Werkstätte und suchen hierfür Auszubildende in folgenden Berufen:
Kfz-Mechatroniker, Automobilkaufmann, Fachkraft für Lagerlogistik.
Aufgabenstellung
Die Post sollen Jugendliche ansprechen und sich an dem bisherigen Layout orientieren.

```html
<!DOCTYPE html>
<html lang="de">
<head>
<meta charset="utf-8">
<title>Ausbildung bei auto-wendlar</title>
<link rel="stylesheet" href="https://fonts.googleapis.com/css2?family=Roboto:wght@300;400;700;900&display=swap">
<style>
  :root {
    --ink: #0d0d0d;
    --navy: #1c2d6b;
    --navy-soft: #2a3f86;
    --accent: #f2ec1c;
    --white: #ffffff;
    --fade: #f4f4f4;
  }
  * { margin: 0; padding: 0; box-sizing: border-box; }
  html, body { width: 1200px; height: 1200px; overflow: hidden; }
  body { font-family: "Roboto", Arial, sans-serif; color: var(--ink); background: var(--white); }

  .post { position: relative; width: 1200px; height: 1200px; overflow: hidden; }

  .photo {
    position: absolute; inset: 0;
    background:
      linear-gradient(90deg, rgba(255,255,255,1) 0%, rgba(255,255,255,.92) 35%, rgba(255,255,255,.35) 55%, rgba(255,255,255,0) 70%),
      linear-gradient(160deg, #d9d9d9 0%, #a9a9a9 40%, #7a7670 70%, #d6d3ce 100%);
  }

  .brand {
    position: absolute; left: 111px; top: 118px;
    font-size: 40px; font-weight: 700; color: var(--navy); letter-spacing: -.5px;
    display: flex; align-items: center; gap: 12px;
  }
  .brand-mark { width: 18px; height: 18px; background: var(--navy); }

  .eyebrow {
    position: absolute; left: 114px; top: 336px;
    font-size: 25px; font-weight: 300; letter-spacing: 2.5px;
  }

  .headline {
    position: absolute; left: 110px; top: 412px;
    font-size: 91px; font-weight: 900; line-height: 80px; letter-spacing: 1px;
    text-transform: uppercase;
  }
  .headline .slash {
    display: inline-block; width: 14px; height: 40px; margin-left: 20px;
    background: var(--accent); transform: skewX(-22deg); vertical-align: -4px;
  }

  .jobs {
    position: absolute; left: 112px; top: 696px;
    list-style: none; font-size: 40px; font-weight: 400; line-height: 64px;
  }

  .cta {
    position: absolute; left: 112px; top: 913px; width: 538px; height: 84px;
    border-radius: 42px; background: var(--navy); color: var(--white);
    display: flex; align-items: center; justify-content: center; padding-right: 110px;
    font-size: 26px; font-weight: 700; letter-spacing: 1px; text-decoration: none;
  }

  .contact { position: absolute; top: 1091px; display: flex; align-items: center; gap: 20px; font-size: 24px; }
  .contact-web { left: 112px; }
  .contact-mail { left: 590px; }
  .contact-icon { width: 52px; height: 52px; }

  .chevrons { position: absolute; left: 1024px; top: 1100px; width: 72px; height: 40px; }
</style>
</head>
<body>
<main class="post">
  <div class="photo" role="img" aria-label="Foto: junge Mechatronikerin in grauer Latzhose und Kappe mit Schraubenschlüssel vor einem Auto in der Werkstatt"></div>

  <div class="brand"><span class="brand-mark"></span>auto-wendlar</div>

  <p class="eyebrow">AUSBILDUNG</p>

  <h1 class="headline">Lust auf<br>eine Ausbildung<br>bei uns?<span class="slash"></span></h1>

  <ul class="jobs">
    <li>KFZ-Mechatroniker (m/w/d) /</li>
    <li>Automobilkaufmann (m/w/d) /</li>
    <li>Fachkraft für Lagerlogistik (m/w/d)</li>
  </ul>

  <a class="cta" href="#">JETZT BEWERBEN !</a>

  <div class="contact contact-web">
    <svg class="contact-icon" viewBox="0 0 52 52" aria-hidden="true">
      <circle cx="26" cy="26" r="26" fill="#1c2d6b"/>
      <g fill="none" stroke="#fff" stroke-width="2">
        <circle cx="26" cy="26" r="13"/>
        <ellipse cx="26" cy="26" rx="6" ry="13"/>
        <line x1="13" y1="26" x2="39" y2="26"/>
        <line x1="15" y1="19" x2="37" y2="19"/>
        <line x1="15" y1="33" x2="37" y2="33"/>
      </g>
    </svg>
    <span>www.kfzjobs.autowendlar.de</span>
  </div>

  <div class="contact contact-mail">
    <svg class="contact-icon" viewBox="0 0 52 52" aria-hidden="true">
      <circle cx="26" cy="26" r="26" fill="#1c2d6b"/>
      <circle cx="26" cy="26" r="17" fill="none" stroke="#fff" stroke-width="2"/>
      <rect x="17" y="20" width="18" height="13" rx="1.5" fill="#fff"/>
      <polyline points="17,21 26,28 35,21" fill="none" stroke="#1c2d6b" stroke-width="1.6"/>
    </svg>
    <span>jwendlar@autowendlar.de</span>
  </div>

  <svg class="chevrons" viewBox="0 0 72 40" aria-hidden="true">
    <g fill="none" stroke="#f2ec1c" stroke-width="3">
      <polyline points="4,4 18,20 4,36"/>
      <polyline points="27,4 41,20 27,36"/>
      <polyline points="50,4 64,20 50,36"/>
    </g>
  </svg>
</main>
</body>
</html>
```